Velvet Crest Car Detailing Brochure

I would like a trifold brochure designed for my car detailing business. The background has to be full black or mostly black with some designing using only colors present in our logo.

Front page must have our logo and name, list of services, a photo and mybe our phone number but no long text.

Inside I want to present each service one by one with its description and a photo representing/showing each service. (I will provide the text below). For photos, use stock photos and I will add come of mines already too.

On the back of the brochure I want to have contact & info: phone number, opening hours, address, website, Instagram.

Outside left I want the text About us and photo/design.

I want the brochure to be neat, professional, easy to read, but at the same time not too boring.

Text:
1. About us
a. the ultimate destination for car care in Geneva. We provide personalized, detail-oriented services that bring out the best in your car. With our expert techniques and dedicated approach, we ensure that your car receives the utmost care and attention. Experience a place where passion meets precision and let us create an exceptional car care experience designed just for you.
2. Services:

DETAILING & HAND WASH

• Comprehensive exterior & interior care
• Personalisation and tailored cleaning packages
• Decontamination
• Premium products
• Attention to detail for a perfect finish

POLISHING

• Eliminates scratches, holograms
• Revives and protects paint
• Ensures lasting gloss
• Enhances paint life
• Preserves car’s value and beauty

CERAMIC TREATMENT

• Durable paint protection
• Water-repellent (hydrophobic) effect
• Easier cleaning, enhanced shine
• Long-term surface safeguarding
• Shields against environmental impacts

DRY ICE WASH

• Innovative, waterless method
• Safe for all car parts
• Deep cleans, removes odors
• Allergen-free, antibacterial
• Gentle, effective
• Advanced cleaning technology

COVERING

• Personalized vehicle styling
• More than 150 colours available
• Clean cut without using a cutter
• High-quality, durable materials
• Custom designs available

PROTECTION FILM

• Invisible, durable shield
• Self-healing technology
• 10-year warranty by QR VONT

DETAILING BOUTIQUE

• Premium brands available
• Buy on site during your visit
• Marble Harbour, Zeb Autos, DRUP Polaro
• Essential for at-home car care
• Perfect for quick touch-ups
(for these three brands you can put their logos

Target Market(s)

Our target market includes car owners of all price ranges, with a special focus on those who are passionate about their vehicles. We cater to clients who value excellent service and results, and seek to maintain their cars in pristine condition.

Industry/Entity Type

Automobile / Car detailing

Colors

Designer to choose colors to be used in the design.

Requirements
Must have
• Brand Consistency: The brochure must adhere to our brand colors and style, particularly utilizing the colors present in our logo. Trifold Layout: The design must be specifically tailored for a trifold brochure format. Legibility: Text must be easy to read against the mostly black background, with appropriate font size and style. Professional Look and Feel: The overall design must convey professionalism while being engaging and not overly complex. Photo representation: each service description should have a phot presenting it.
Should not have
• Overcrowded Design: Avoid cluttering with too much text or too many images. The layout should be clean and easy to navigate. Cartoonish Fonts or Graphics: Avoid using unprofessional or casual fonts and graphics that do not align with the upscale and professional image of our business. Distracting Backgrounds: The background should complement and not overpower the content. Stick to the theme of mostly black with design elements from our logo.

```html
<!DOCTYPE html>
<html lang="en">
<head>
<meta charset="utf-8">
<title>Velvet Crest Car Detailing – Trifold Brochure</title>
<link rel="stylesheet" href="https://fonts.googleapis.com/css2?family=Josefin+Sans:ital,wght@0,400;0,600;0,700;1,700&family=Jost:ital,wght@0,400;0,500;1,400&display=swap">
<style>
  :root{
    --page:#eceef1;
    --ink:#0b0b0e;
    --panel:#111114;
    --text:#e9e9ee;
    --muted:#b9b9c4;
    --blue:#3f8fe6;
    --violet:#8b45dc;
    --magenta:#d23ad8;
    --pill:#b24ce2;
    --fold:rgba(255,255,255,.06);
  }
  *{box-sizing:border-box;margin:0;padding:0}
  html,body{width:1200px;height:2399px;overflow:hidden}
  body{background:var(--page);font-family:"Jost",sans-serif;color:var(--text);position:relative}

  .spread{position:absolute;left:50px;width:1100px;height:850px;background:var(--ink);
    display:grid;grid-template-columns:repeat(3,1fr);box-shadow:0 20px 50px rgba(0,0,0,.25)}
  .spread--outside{top:150px}
  .spread--inside{top:1250px}
  .panel{position:relative;padding:44px 34px;border-right:1px solid var(--fold);overflow:hidden}
  .panel:last-child{border-right:none}

  .photo{border-radius:14px;display:block}

  /* brand name block */
  .brand{display:flex;align-items:center;gap:12px;justify-content:center}
  .brand__dot{width:46px;height:46px;border-radius:50%;border:3px solid var(--violet)}
  .brand__name{font-family:"Josefin Sans",sans-serif;font-weight:400;font-size:22px;letter-spacing:.08em;color:var(--text);line-height:1.1;text-transform:uppercase}

  /* about panel */
  .about__title{font-family:"Josefin Sans",sans-serif;font-style:italic;font-weight:700;font-size:34px;color:var(--magenta);margin-bottom:16px}
  .about__text{font-style:italic;font-size:14px;line-height:1.6;color:var(--muted)}
  .about__photo{margin-top:28px;height:230px;background:linear-gradient(135deg,#6b6f77,#2b2d33 55%,#4a88c4)}
  .about__seat{position:absolute;left:0;right:0;bottom:0;height:260px;background:linear-gradient(180deg,transparent,#1c1c20 40%,#26262b)}

  /* contact panel */
  .contact{display:flex;flex-direction:column;align-items:center;text-align:center}
  .contact .brand{margin-top:90px;flex-direction:column;gap:8px}
  .hours{margin-top:40px;width:100%;height:150px;border:1.5px solid var(--blue);border-radius:16px;position:relative}
  .hours__label{position:absolute;top:-10px;left:50%;transform:translateX(-50%);background:var(--ink);padding:0 10px;
    font-family:"Josefin Sans",sans-serif;font-weight:700;font-size:14px;letter-spacing:.06em;color:var(--blue);text-transform:uppercase}
  .contact__title{margin-top:70px;font-family:"Josefin Sans",sans-serif;font-weight:700;font-size:15px;letter-spacing:.08em;color:var(--blue);text-transform:uppercase}
  .icons{display:flex;gap:10px;margin:10px 0 12px}
  .icons svg{width:22px;height:22px}
  .contact__list{list-style:none;font-size:13px;line-height:1.65;color:var(--text)}

  /* cover panel */
  .cover{padding:0;display:flex;flex-direction:column;align-items:center}
  .cover__photo{width:100%;height:400px;background:radial-gradient(ellipse at 55% 70%,#ff7a2e 0,#b9331a 8%,transparent 22%),linear-gradient(160deg,#2e3036,#141418 60%,#0b0b0e)}
  .cover .brand{margin-top:10px;flex-direction:column;gap:8px}
  .cover__services{margin-top:26px;text-align:center;font-family:"Josefin Sans",sans-serif;font-size:16px;line-height:1.45;letter-spacing:.03em;text-transform:uppercase;padding:0 24px}
  .cover__services .sep{color:var(--violet);font-weight:700}
  .phone-pill{margin-top:28px;display:flex;align-items:center;gap:8px;background:var(--pill);border-radius:30px;padding:8px 26px;
    font-family:"Josefin Sans",sans-serif;font-weight:700;font-size:26px;color:#fff;letter-spacing:.04em}
  .phone-pill svg{width:22px;height:22px}

  /* services */
  .services__title{font-family:"Josefin Sans",sans-serif;font-weight:700;font-size:28px;color:var(--violet);text-transform:uppercase;margin-bottom:18px}
  .service{margin-bottom:16px}
  .service__name{font-family:"Josefin Sans",sans-serif;font-weight:600;font-size:16px;letter-spacing:.05em;color:var(--blue);text-transform:uppercase;margin-bottom:6px}
  .ticks{list-style:none;font-size:13px;line-height:1.55;color:var(--text)}
  .ticks li{position:relative;padding-left:20px}
  .ticks li::before{content:"";position:absolute;left:0;top:4px;width:11px;height:11px;border:1.5px solid var(--blue);border-radius:2px}
  .ticks li::after{content:"";position:absolute;left:4px;top:5px;width:4px;height:7px;border:solid var(--violet);border-width:0 2px 2px 0;transform:rotate(40deg)}
  .service-photo{height:150px;margin:10px 0 20px}
  .photo--wash{background:linear-gradient(135deg,#d9dce2,#6c7078 45%,#1d1e22)}
  .photo--polish{background:linear-gradient(135deg,#3a3b40,#e0782a 45%,#1a1a1e)}
  .photo--ceramic{background:linear-gradient(135deg,#2b6fc2,#575b63 55%,#1c1d21)}
  .photo--film{background:linear-gradient(135deg,#4fcf52,#d8dade 40%,#383a40)}
  .photo--covering{background:linear-gradient(135deg,#e7c3a6,#6d7078 50%,#222327)}
  .brands{display:flex;flex-wrap:wrap;gap:14px 22px;margin-top:20px;align-items:center}
  .brands span{font-family:"Jost",sans-serif;font-weight:500;font-size:15px;color:var(--text);letter-spacing:.04em}
  .boutique-bg{position:absolute;left:0;right:0;bottom:0;height:230px;background:linear-gradient(180deg,transparent,#1b1c21)}
</style>
</head>
<body>

<!-- Outside spread -->
<section class="spread spread--outside">
  <article class="panel about">
    <h2 class="about__title">About us</h2>
    <p class="about__text">The ultimate destination for car care in Geneva. We provide personalized, detail-oriented services that bring out the best in your car. With our expert techniques and dedicated approach, we ensure that your car receives the utmost care and attention. Experience a place where passion meets precision and let us create an exceptional car care experience designed just for you.</p>
    <div class="about__seat" role="img" aria-label="Dark leather car seat texture"></div>
    <div class="photo about__photo" role="img" aria-label="Detailer cleaning a car interior and wheel"></div>
  </article>

  <article class="panel contact">
    <div class="brand">
      <span class="brand__dot"></span>
      <span class="brand__name">Velvet<br>Crest</span>
    </div>
    <div class="hours"><span class="hours__label">Opening hours</span></div>
    <h3 class="contact__title">Contact</h3>
    <div class="icons">
      <svg viewBox="0 0 24 24"><circle cx="12" cy="12" r="11" fill="none" stroke="#3f8fe6" stroke-width="1.5"/><path d="M8 7l2 0 1 3-1.5 1a7 7 0 0 0 3.5 3.5l1-1.5 3 1v2a1 1 0 0 1-1 1A10 10 0 0 1 7 8a1 1 0 0 1 1-1z" fill="#8b45dc"/></svg>
      <svg viewBox="0 0 24 24"><circle cx="12" cy="12" r="11" fill="none" stroke="#3f8fe6" stroke-width="1.5"/><rect x="6" y="8" width="12" height="8" rx="1" fill="none" stroke="#8b45dc" stroke-width="1.5"/><path d="M6 8l6 5 6-5" fill="none" stroke="#8b45dc" stroke-width="1.5"/></svg>
      <svg viewBox="0 0 24 24"><circle cx="12" cy="12" r="11" fill="none" stroke="#3f8fe6" stroke-width="1.5"/><circle cx="12" cy="12" r="5.5" fill="none" stroke="#8b45dc" stroke-width="1.5"/><path d="M6.5 12h11M12 6.5v11" stroke="#8b45dc" stroke-width="1.2"/></svg>
      <svg viewBox="0 0 24 24"><circle cx="12" cy="12" r="11" fill="none" stroke="#3f8fe6" stroke-width="1.5"/><circle cx="12" cy="12" r="4" fill="#8b45dc"/></svg>
      <svg viewBox="0 0 24 24"><circle cx="12" cy="12" r="11" fill="none" stroke="#3f8fe6" stroke-width="1.5"/><path d="M12 18s-5-5-5-8a5 5 0 0 1 10 0c0 3-5 8-5 8z" fill="#8b45dc"/><circle cx="12" cy="10" r="1.8" fill="#0b0b0e"/></svg>
    </div>
    <ul class="contact__list">
      <li>+41795550123</li>
      <li>hello@velvetcrest.ch</li>
      <li>www.velvetcrest.ch</li>
      <li>www.instagram.com/velvetcrest.gva</li>
      <li>Rue des Tilleuls 8, 1227 Carouge</li>
    </ul>
  </article>

  <article class="panel cover">
    <div class="cover__photo" role="img" aria-label="Close-up of a black sports car with a glowing orange tail light"></div>
    <div class="brand">
      <span class="brand__dot"></span>
      <span class="brand__name">Velvet<br>Crest</span>
    </div>
    <p class="cover__services">Detailing &amp; hand wash <span class="sep">||</span> Polishing<br>Ceramic treatment <span class="sep">||</span> Dry ice wash<br>Covering <span class="sep">||</span> Protection film<br>Detailing boutique</p>
    <div class="phone-pill">
      <svg viewBox="0 0 24 24"><path d="M6 3l4 0 1.5 5-2.5 1.5a11 11 0 0 0 5.5 5.5L16 12.5l5 1.5v4a2 2 0 0 1-2 2A17 17 0 0 1 4 5a2 2 0 0 1 2-2z" fill="#fff"/></svg>
      41795550123
    </div>
  </article>
</section>

<!-- Inside spread -->
<section class="spread spread--inside">
  <article class="panel services">
    <h2 class="services__title">Our services:</h2>
    <div class="service">
      <h3 class="service__name">Detailing &amp; hand wash</h3>
      <ul class="ticks">
        <li>Comprehensive exterior &amp; interior care</li>
        <li>Personalisation and tailored cleaning packages</li>
        <li>Decontamination</li>
        <li>Premium products</li>
        <li>Attention to detail for a perfect finish</li>
      </ul>
    </div>
    <div class="photo service-photo photo--wash" role="img" aria-label="Wheel being hand washed with a brush and foam"></div>
    <div class="service">
      <h3 class="service__name">Polishing</h3>
      <ul class="ticks">
        <li>Eliminates scratches, holograms</li>
        <li>Revives and protects paint</li>
        <li>Ensures lasting gloss</li>
        <li>Enhances paint life</li>
        <li>Preserves car’s value and beauty</li>
      </ul>
    </div>
    <div class="photo service-photo photo--polish" role="img" aria-label="Orange microfibre polishing cloth on a dark car bonnet"></div>
  </article>

  <article class="panel services">
    <div class="service">
      <h3 class="service__name">Ceramic treatment</h3>
      <ul class="ticks">
        <li>Durable paint protection</li>
        <li>Water-repellent (hydrophobic) effect</li>
        <li>Easier cleaning, enhanced shine</li>
        <li>Long-term surface safeguarding</li>
        <li>Shields against environmental impacts</li>
      </ul>
    </div>
    <div class="photo service-photo photo--ceramic" role="img" aria-label="Polishing pad and ceramic coating bottle"></div>
    <div class="service">
      <h3 class="service__name">Dry ice wash</h3>
      <ul class="ticks">
        <li>Innovative, waterless method</li>
        <li>Safe for all car parts</li>
        <li>Deep cleans, removes odors</li>
        <li>Allergen-free, antibacterial</li>
        <li>Gentle, effective</li>
        <li>Advanced cleaning technology</li>
      </ul>
    </div>
    <div class="service">
      <h3 class="service__name">Protection film</h3>
      <ul class="ticks">
        <li>Invisible, durable shield</li>
        <li>Self-healing technology</li>
        <li>10-year warranty by QR VONT</li>
      </ul>
    </div>
    <div class="photo service-photo photo--film" role="img" aria-label="Dry ice wash and protection film being applied to a car"></div>
  </article>

  <article class="panel services">
    <div class="service">
      <h3 class="service__name">Covering</h3>
      <ul class="ticks">
        <li>Personalized vehicle styling</li>
        <li>More than 150 colours available</li>
        <li>Clean cut without using a cutter</li>
        <li>High-quality, durable materials</li>
        <li>Custom designs available</li>
      </ul>
    </div>
    <div class="photo service-photo photo--covering" role="img" aria-label="Hand applying vinyl wrap around a car headlight"></div>
    <div class="boutique-bg" role="img" aria-label="Dark glossy car body in low light"></div>
    <div class="service">
      <h3 class="service__name">Detailing boutique</h3>
      <ul class="ticks">
        <li>Premium brands available</li>
        <li>Buy on site during your visit</li>
        <li>Essential for at-home car care</li>
        <li>Perfect for quick touch-ups</li>
        <li>Marble Harbour, Zeb Autos, DRUP Polaro</li>
      </ul>
    </div>
    <div class="brands">
      <span>Marble Harbour</span>
      <span>Zeb Autos</span>
      <span>DRUP Polaro</span>
    </div>
  </article>
</section>

</body>
</html>
```